“Bright Tide” Spring Fair Poster

We are putting together a school and community fair. We need a poster designed to advertise the event and give some important information to would be attendees. We’d like the poster graphics to evoke a minimalistic and futuristic aesthetic, be bold, yet fun! We will printing the posters, so we will need for them to be at high resolution and ready to send to print.

Target Market(s)

Students, Parents, and Community members

Industry/Entity Type

School

Font styles to use
Sans Serif

Colors
33a6d7
fabb78
9d9d9d
ffffff
1b1b1b
33b8a4

Requirements
Must have
• Bright Tide
• Birch & Lantern Spring Fair 2018
• Friday, May 18th
• 5:00-9:00pm
• Tickets Will Be Available at Select Pick up & Drop Off Times
• Come Enjoy a Futuristic Evening of Food, Music, Entertainment, & Fun!
Nice to have
• We’d love to see a bold and graphic poster with a futuristic feel!
• See the sample image below from previous event poster and additional images for mood and inspiration. Would love to see metallics (silver or metallic colors)

```html
<!DOCTYPE html>
<html lang="en">
<head>
<meta charset="utf-8">
<title>Bright Tide — Birch &amp; Lantern Spring Fair 2018</title>
<link rel="stylesheet" href="https://fonts.googleapis.com/css2?family=Big+Shoulders+Display:wght@600&family=Questrial&family=Bebas+Neue&display=swap">
<style>
  :root {
    --sky-deep: #0a2763;
    --sky-mid: #1553b4;
    --sky-glow: #2a7fe0;
    --neon-cyan: #47cff5;
    --peach: #f6b66c;
    --rule-white: #ffffff;
  }
  html, body {
    margin: 0;
    padding: 0;
    width: 927px;
    height: 1200px;
    overflow: hidden;
    background: var(--sky-deep);
  }
  .poster {
    position: relative;
    width: 927px;
    height: 1200px;
    overflow: hidden;
    background: radial-gradient(ellipse 620px 560px at 50% 46%, var(--sky-glow) 0%, var(--sky-mid) 45%, var(--sky-deep) 100%);
    text-align: center;
  }
  .event-title {
    position: absolute;
    top: 32px;
    left: 0;
    width: 100%;
    margin: 0;
    font-family: "Big Shoulders Display", "Arial Narrow", sans-serif;
    font-weight: 600;
    font-size: 268px;
    line-height: 1;
    white-space: nowrap;
    text-transform: uppercase;
    color: var(--neon-cyan);
  }
  .event-title__text {
    display: inline-block;
    letter-spacing: 4px;
    transform: scaleX(0.76);
    transform-origin: 50% 50%;
  }
  .fair-name {
    position: absolute;
    top: 276px;
    left: 0;
    width: 100%;
    margin: 0;
    font-family: "Questrial", sans-serif;
    font-size: 40px;
    font-variant: small-caps;
    letter-spacing: 5px;
    white-space: nowrap;
    color: var(--peach);
  }
  .event-date, .event-time {
    position: absolute;
    left: 0;
    width: 100%;
    margin: 0;
    font-family: "Questrial", sans-serif;
    color: var(--peach);
    white-space: nowrap;
  }
  .event-date { top: 362px; font-size: 50px; font-variant: small-caps; letter-spacing: 6.5px; }
  .event-time { top: 424px; font-size: 52px; letter-spacing: 8px; }
  .rule {
    position: absolute;
    left: 225px;
    width: 477px;
    height: 4px;
    background: var(--rule-white);
  }
  .rule--one { top: 529px; }
  .rule--two { top: 647px; }
  .rule--three { top: 769px; }
  .info {
    position: absolute;
    left: 0;
    width: 100%;
    margin: 0;
    font-family: "Bebas Neue", sans-serif;
    font-size: 36px;
    line-height: 42px;
    letter-spacing: 1.5px;
    white-space: nowrap;
    color: var(--peach);
  }
  .info--tickets { top: 545px; }
  .info--invite { top: 663px; }
  .skyline-art {
    position: absolute;
    left: 0;
    top: 800px;
    width: 927px;
    height: 400px;
    background: linear-gradient(to bottom, rgba(71, 207, 245, 0) 0%, rgba(71, 207, 245, 0.55) 35%, var(--neon-cyan) 70%);
  }
</style>
</head>
<body>
  <main class="poster">
    <h1 class="event-title"><span class="event-title__text">Bright Tide</span></h1>
    <p class="fair-name">Birch &amp; Lantern Spring Fair 2018</p>
    <p class="event-date">Friday, May 18th</p>
    <p class="event-time">5:00–9:00 PM</p>

    <div class="rule rule--one"></div>
    <p class="info info--tickets">Tickets will be available at select<br>pick up &amp; drop off times</p>
    <div class="rule rule--two"></div>
    <p class="info info--invite">Come enjoy a futuristic evening of<br>food, music, entertainment, &amp; fun!</p>
    <div class="rule rule--three"></div>

    <div class="skyline-art" role="img" aria-label="Silhouette of a futuristic city skyline with towers and spires, with small spaceships flying above it"></div>
  </main>
</body>
</html>
```